'Wedding Business" Business Card Design

dj services for weddings and parties, uplighting, event planning, day of coordination for weddings, photography for weddings and other events.

Would like raised print and metallic also if possible. Elegant design, yet modern. This is a wedding business and should describe our goals and main services - DJ/lighting, wedding and event planning, photography. slogan "Simply Incredible, Incredibly simple" or "Your Dreams. Our Experience. The Perfect Match" Our goal is to provide multiple services to make it easier for the bride and groom almost like a one stop shop. Feel free to use the slogan or leave it out , we just want to really stand out against the competition. You can also get more info on our website www.brightlanestudios.com - we are working to get the brightlanenc.com site pointed to our current site!

there should be 2 files attached, if they did not go through please email events@brightlanenc.com or brightlanestudios@mailbox.test
Updates

Thank you all for your help, we have decided what we like but would like to make some changes, we need to order these asap so please let us know if you can help.

Reason: Wasn't able to pick it out in time! So Sorry but we know what we want!!

Industry/Entity Type

Business

Contact Information for Business Card

Marcus and Leona Whitcombe
555-318-2047
555-720-4861
Bright Lane Studios, Events, & Photography
EMAIL:Events@BrightLaneNC.com
www.brightlanenc.com

```html
<!DOCTYPE html>
<html lang="en">
<head>
<meta charset="utf-8">
<title>Bright Lane Studios – Business Card</title>
<link rel="stylesheet" href="https://fonts.googleapis.com/css2?family=Alegreya:ital,wght@0,400;1,400&family=Merienda:wght@500&display=swap">
<style>
  :root{
    --card-black:#060606;
    --royal-blue:#323e98;
    --paper-white:#ffffff;
    --silver:#c8ccd4;
    --backdrop:#d8d3cb;
    --card-w:540px;
    --card-h:309px;
  }
  *{box-sizing:border-box;margin:0;padding:0}
  html,body{width:1200px;height:858px;overflow:hidden;background:var(--backdrop)}
  .stage{position:relative;width:1200px;height:858px}

  .card{
    position:absolute;top:274px;width:var(--card-w);height:var(--card-h);
    background:var(--card-black);overflow:hidden;
    box-shadow:0 10px 24px rgba(0,0,0,.28);
  }
  .card--front{left:40px}
  .card--back{left:620px}

  .front-panels{position:absolute;inset:0}

  .wordmark{
    position:absolute;font-family:"Alegreya",serif;font-weight:400;color:var(--silver);
    line-height:1;letter-spacing:.5px;
  }
  .wordmark--small{left:24px;top:44px;font-size:30px;line-height:1.05}

  .services{
    position:absolute;left:196px;top:36px;list-style:none;
    font-family:"Alegreya",serif;font-size:16px;color:var(--paper-white);line-height:23px;
  }
  .services li::before{content:"*";display:inline-block;width:16px;font-size:14px}

  .owners{
    position:absolute;right:16px;top:178px;text-align:right;
    font-family:"Merienda",cursive;font-weight:500;font-size:17px;color:var(--royal-blue);line-height:38px;
  }

  .contact{
    position:absolute;left:62px;top:186px;list-style:none;
    font-family:"Alegreya",serif;font-size:14.5px;color:var(--paper-white);line-height:20px;
  }
  .contact li{display:flex;align-items:center;gap:8px}
  .contact svg{width:11px;height:11px;flex:none}

  .back-stripe{position:absolute;left:0;right:0;bottom:0;height:30px;background:var(--royal-blue)}
  .back-rule{position:absolute;left:0;right:0;bottom:34px;height:3px;background:var(--paper-white)}
  .wordmark--large{left:0;right:0;top:104px;text-align:center;font-size:58px}
</style>
</head>
<body>
<main class="stage">

  <section class="card card--front" aria-label="Business card front">
    <svg class="front-panels" viewBox="0 0 540 309" preserveAspectRatio="none" aria-hidden="true">
      <polygon points="0,148 300,142 405,309 0,309" fill="var(--royal-blue)"/>
      <polygon points="300,142 540,142 540,309 405,309" fill="var(--paper-white)"/>
    </svg>

    <p class="wordmark wordmark--small">Bright<br>Lane</p>

    <ul class="services">
      <li>Bright Lane Studios</li>
      <li>Events</li>
      <li>Photography</li>
    </ul>

    <p class="owners">Marcus<br>Leona Whitcombe</p>

    <ul class="contact">
      <li>
        <svg viewBox="0 0 12 12" aria-hidden="true"><path d="M3 1l2 2.4-1.2 1.3c.6 1.4 1.8 2.6 3.2 3.2L8.3 6.7 11 8.6 9.6 11C5 10.6 1.4 7 1 2.4z" fill="#fff"/></svg>
        555-318-2047
      </li>
      <li>
        <svg viewBox="0 0 12 12" aria-hidden="true"><path d="M3 1l2 2.4-1.2 1.3c.6 1.4 1.8 2.6 3.2 3.2L8.3 6.7 11 8.6 9.6 11C5 10.6 1.4 7 1 2.4z" fill="#fff"/></svg>
        555-720-4861
      </li>
      <li>
        <svg viewBox="0 0 12 12" aria-hidden="true"><circle cx="6" cy="6" r="5" fill="none" stroke="#fff" stroke-width="1.3"/><ellipse cx="6" cy="6" rx="2.2" ry="5" fill="none" stroke="#fff" stroke-width="1"/><line x1="1" y1="6" x2="11" y2="6" stroke="#fff" stroke-width="1"/></svg>
        www.brightlanenc.com
      </li>
      <li>
        <svg viewBox="0 0 12 12" aria-hidden="true"><rect x="1" y="2.5" width="10" height="7" fill="#fff"/><path d="M1 2.5l5 4 5-4" fill="none" stroke="var(--royal-blue)" stroke-width="1"/></svg>
        Events@BrightLaneNC.com
      </li>
    </ul>
  </section>

  <section class="card card--back" aria-label="Business card back">
    <p class="wordmark wordmark--large">Bright Lane</p>
    <div class="back-rule"></div>
    <div class="back-stripe"></div>
  </section>

</main>
</body>
</html>
```